Clearbrook Lawnworks LLC Business Card

Ok, first off let me thank you for taking the time to participate in this project !! I have my business logo that I want incorporated into business card design . My irrigation business is located in a very upscale part of town and we do high end homes . So with that said I'm planning on these cards being plastic credit card type cards. I would like them to be two sided . I'm thinking something bold , yet classy and clean . Not too busy . We do different types of work . 80% irrigation service and installation . 15% landscape lighting and the other 5% drainage and hardscapes ! I have a website that I want listed on it as well as our address , phone number and of course my name and title .

Target Market(s)

Upscale homeowners and architects

Industry/Entity Type

Landscape

Requirements
Must have
• Company logo, website, address , phone number , name , title , services offered

Www.ClearbrookLawnworks.example
Marcus Hendley owner
205-555-0148
Clearbrook Lawnworks LLC
P.O. Box 478512
Birmingham, Alabama 35213

```html
<!DOCTYPE html>
<html lang="en">
<head>
<meta charset="utf-8">
<title>Clearbrook Lawnworks LLC – Business Cards</title>
<link rel="stylesheet" href="https://fonts.googleapis.com/css2?family=Jost:wght@400;600&display=swap">
<style>
  :root {
    --stage-bg: #3b322c;
    --card-black: #050607;
    --photo-top: #3f6fa8;
    --photo-mid: #2d5a8a;
    --forest: #2c5a45;
    --mark-blue: #2b86d8;
    --mark-ring: #0b1016;
    --brand-green: #7fd63a;
    --accent-cyan: #7fd0f0;
    --text-white: #f4f7fa;
  }
  * { margin: 0; padding: 0; box-sizing: border-box; }
  html, body {
    width: 1200px; height: 812px; overflow: hidden;
    background: var(--stage-bg);
    font-family: "Jost", sans-serif;
  }
  .stage { position: relative; width: 1200px; height: 812px; }

  .card {
    position: absolute;
    width: 519px; height: 296px;
    border-radius: 22px;
    overflow: hidden;
    background: var(--card-black);
    color: var(--text-white);
  }
  .card--front   { left: 48px;  top: 95px; }
  .card--back    { left: 633px; top: 96px; }
  .card--variant { left: 341px; top: 424px; }

  .card__photo {
    position: absolute; left: 0; top: 0; width: 100%;
    background:
      radial-gradient(ellipse 60px 220px at 52% 30%, rgba(140,190,240,.55), transparent 70%),
      linear-gradient(90deg, var(--forest) 0%, var(--photo-mid) 35%, var(--photo-top) 50%, var(--photo-mid) 65%, var(--forest) 100%);
  }
  .card--front .card__photo   { height: 201px; }
  .card--back .card__photo    { height: 79px; }
  .card--variant .card__photo { height: 149px; }

  .card__web {
    position: absolute; left: 0; width: 100%;
    text-align: center; font-size: 20px; font-weight: 400;
  }
  .card--front .card__web   { top: 60px; }
  .card--variant .card__web { top: 30px; }

  .brand-mark {
    position: absolute; border-radius: 50%;
    background: var(--mark-blue);
    border: 8px solid var(--mark-ring);
  }
  .card--front .brand-mark   { width: 106px; height: 106px; left: 207px; top: 143px; }
  .card--back .brand-mark    { width: 122px; height: 122px; left: 199px; top: 18px; }
  .card--variant .brand-mark { width: 156px; height: 156px; left: 182px; top: 73px; }

  .brand-name {
    position: absolute; left: 0; width: 100%;
    text-align: center; font-weight: 600;
    color: var(--brand-green);
  }
  .card--front .brand-name { top: 236px; font-size: 27px; }
  .card--back .brand-name  { top: 132px; font-size: 30px; }

  .card__person {
    position: absolute; left: 150px; width: 292px; text-align: center;
    font-size: 15px; line-height: 21px; top: 201px;
  }
  .card__address {
    position: absolute; left: 10px; width: 200px; top: 242px;
    text-align: center; font-size: 12px; line-height: 15px; font-style: normal;
  }
  .card__contact {
    position: absolute; right: 18px; top: 250px;
    font-size: 12px; line-height: 20px; text-align: left;
  }
  .card__contact li { list-style: none; display: flex; align-items: center; gap: 5px; }
  .card__contact svg { width: 14px; height: 14px; }

  .card__services {
    position: absolute; left: 0; width: 100%; top: 252px;
    text-align: center; font-size: 13px; letter-spacing: .04em;
    color: var(--accent-cyan);
  }
</style>
</head>
<body>
<main class="stage">

  <section class="card card--front" aria-label="Card front">
    <div class="card__photo" role="img" aria-label="Misty forest waterfall behind a stone arch bridge"></div>
    <p class="card__web">Www.ClearbrookLawnworks.example</p>
    <div class="brand-mark" aria-hidden="true"></div>
    <p class="brand-name">Clearbrook Lawnworks</p>
  </section>

  <section class="card card--back" aria-label="Card back">
    <div class="card__photo" role="img" aria-label="Misty forest waterfall behind a stone arch bridge"></div>
    <div class="brand-mark" aria-hidden="true"></div>
    <p class="brand-name">Clearbrook Lawnworks</p>
    <p class="card__person">Marcus Hendley<br>Owner</p>
    <address class="card__address">
      Clearbrook Lawnworks LLC<br>P.O. Box 478512<br>Birmingham, Alabama 35213
    </address>
    <ul class="card__contact">
      <li>
        <svg viewBox="0 0 24 24" aria-hidden="true"><path fill="#7fd0f0" d="M6.6 10.8a15 15 0 0 0 6.6 6.6l2.2-2.2c.3-.3.7-.4 1-.2 1.1.4 2.3.6 3.6.6.6 0 1 .4 1 1V20c0 .6-.4 1-1 1C10.6 21 3 13.4 3 4c0-.6.4-1 1-1h3.5c.6 0 1 .4 1 1 0 1.3.2 2.5.6 3.6.1.3 0 .7-.2 1z"/></svg>
        205-555-0148
      </li>
      <li>
        <svg viewBox="0 0 24 24" aria-hidden="true"><circle cx="12" cy="12" r="4" fill="none" stroke="#7fd0f0" stroke-width="2"/><path d="M16 8v5a3 3 0 0 0 6 0v-1a10 10 0 1 0-4 8" fill="none" stroke="#7fd0f0" stroke-width="2"/></svg>
        Www.ClearbrookLawnworks.example
      </li>
    </ul>
  </section>

  <section class="card card--variant" aria-label="Card front, alternate">
    <div class="card__photo" role="img" aria-label="Misty forest waterfall behind a stone arch bridge"></div>
    <p class="card__web">Www.ClearbrookLawnworks.example</p>
    <div class="brand-mark" aria-hidden="true"></div>
    <p class="card__services">Irrigation · Landscape Lighting · Drainage &amp; Hardscapes</p>
  </section>

</main>
</body>
</html>
```